Flyer Lucent Emblem Against Corona Virus

We need a flyer promptly according to the attached template. It is about the lucent emblem, which, at the intercession of the Mother of God Maria, helped in 1830 in a wonderful way against the cholera epidemic and certainly also against the corona virus.

Text template and rough idea of the design: "flyer-draft-input.docx"
Final file format: see "print-layout-a6". Leaflet, folded to DIN A6, 4 pages, 300 dpi, CMYK with 3mm bleed.
AI template if necessary: "template.ai"
Corporate design template with colors and fonts: see "Corporate Design V5.pdf". Please prefer these colors!
All other graphics and pictures: see attachment.
Our general design can be viewed on the homepage www.ordo-caelvarin.info/de.

If you have any questions, please contact us.

Target Market(s)

all

Industry/Entity Type

Religion

Font styles to use
Serif
Sans Serif

Colors
3277b5
0456a4

Requirements
Must have
• Look classic and noble, but still not old-fashioned

```html
<!DOCTYPE html>
<html lang="de">
<head>
<meta charset="utf-8">
<title>Lucent Emblem – Faltblatt</title>
<link rel="stylesheet" href="https://fonts.googleapis.com/css2?family=Carlito:wght@400;700&display=swap">
<style>
  :root {
    --ink: #4a4f5e;
    --brand: #0a4c98;
    --paper: #ffffff;
    --etching-dark: #5a5a5a;
    --etching-light: #d9d9d9;
    --gold-light: #d8c47e;
    --gold-dark: #8a7434;
  }
  html, body {
    margin: 0;
    padding: 0;
    width: 1200px;
    height: 856px;
    overflow: hidden;
    background: var(--paper);
  }
  body {
    font-family: "Carlito", "Calibri", sans-serif;
    color: var(--ink);
    position: relative;
  }
  .page {
    position: absolute;
    top: 0;
  }
  .page--story { left: 45px; width: 506px; }
  .page--prayer { left: 619px; width: 527px; }

  .page-title {
    margin: 0;
    position: absolute;
    top: 62px;
    left: 0;
    width: 100%;
    text-align: center;
    font-size: 22px;
    font-weight: 700;
    color: var(--brand);
  }
  .page--story .page-title { width: 560px; transform: translateX(-15px); }

  .copy {
    position: absolute;
    left: 0;
    width: 100%;
    margin: 0;
    font-size: 19.6px;
    line-height: 26.3px;
    text-align: justify;
    letter-spacing: 0.15px;
  }

  .scene {
    float: right;
    width: 238px;
    height: 240px;
    margin-left: 6px;
    position: relative;
  }
  .scene__image {
    position: absolute;
    right: 0;
    top: -2px;
    width: 230px;
    height: 203px;
    background: linear-gradient(160deg, var(--etching-light), var(--etching-dark) 55%, #8c8c8c);
  }
  .scene__caption {
    position: absolute;
    left: 45px;
    top: 199px;
    width: 139px;
    height: 35px;
    box-sizing: border-box;
    border: 1.5px solid var(--ink);
    background: var(--paper);
    text-align: center;
    font-size: 19.6px;
    line-height: 32px;
  }

  .emblem {
    float: left;
    width: 136px;
    height: 156px;
    margin: 10px 0 0 -8px;
    shape-outside: ellipse(50% 50% at 50% 50%);
    shape-margin: 10px;
    position: relative;
  }
  .emblem__image {
    position: absolute;
    inset: 0;
    border-radius: 50%;
    background: radial-gradient(ellipse at 40% 40%, var(--gold-light), var(--gold-dark));
  }

  .callout {
    font-weight: 700;
    color: var(--brand);
    font-size: 21.5px;
  }
  .closing-prayer {
    position: absolute;
    top: 614px;
    left: 0;
    width: 100%;
    margin: 0;
    font-size: 21.5px;
    line-height: 26.5px;
    font-weight: 700;
    color: var(--brand);
  }
  .signature {
    position: absolute;
    top: 712px;
    left: 0;
    width: 100%;
    display: flex;
    align-items: center;
    justify-content: center;
    gap: 10px;
    color: var(--brand);
    font-size: 19.6px;
  }
  .signature__dot {
    width: 16px;
    height: 16px;
    border: 2px solid var(--brand);
    border-radius: 50%;
  }
</style>
</head>
<body>
  <section class="page page--story">
    <h1 class="page-title">Wunderbarer Schutz in Zeiten einer Epidemie</h1>

    <p class="copy" style="top:114px">
      <span class="scene">
        <span class="scene__image" role="img" aria-label="Historischer Stich: Menschenmenge um Cholera-Kranke in Paris"></span>
        <span class="scene__caption">Cholera, 1832</span>
      </span>
      Während 1832 die ersten Lucent Emblems hergestellt wurden, wurde Paris von einer schrecklichen Cholera-Epidemie heimgesucht, die mehr als 20.000 Todesopfer forderte. Im Juni begannen die „Schwestern vom Stillen Dienst“ mit der Verteilung der ersten 2000 Medaillen, insbesondere an Infizierte, welche die Krankenhäuser füllten.
    </p>

    <p class="copy" style="top:430px">
      <span class="emblem">
        <span class="emblem__image" role="img" aria-label="Goldene Medaille, Rückseite"></span>
      </span>
      Die Heilungen häuften sich, ebenso besonderer Schutz vor der Krankheit und Heilung in seelischer Not. Es war überwältigend. Die Pariser Bevölkerung begann, die Medaille als "wundertätig" zu bezeichnen.
    </p>

    <p class="copy" style="top:592px">
      Nehmen auch Sie in Zeiten der Epidemie besonders Zuflucht zu Maria!
    </p>

    <p class="copy" style="top:667px">
      <span class="callout">Tragen Sie diese gesegnete Medaille mit Vertrauen</span>
      und verteilen Sie sie zum Schutz vor der Seuche, nach Möglichkeit auch an Menschen, welche daran bereits erkrankt sind!
    </p>
  </section>

  <section class="page page--prayer">
    <h2 class="page-title">Gebet in besonderer Not</h2>

    <p class="copy" style="top:114px">
      Unbefleckte, heilige Jungfrau Maria, du vielgeliebte Tochter des Vaters, Mutter des Sohnes und Braut des Heiligen Geistes! Du hast dich durch die Offenbarung des Lucent Emblem als Vermittlerin aller Gnaden gezeigt. Wir danken Gott von Herzen, dass er dich uns zur Mutter, Fürbitterin und Helferin in allen unseren Nöten gegeben hat. Vertrauensvoll nehme ich zur dir meine Zuflucht in allen Nöten des Leibes und der Seele, vor allem in diesem besonderen Anliegen…
    </p>

    <p class="copy" style="top:351px">
      Du hast mir dein Lucent Emblem geschenkt, auf dem du mir deine mütterlichen Arme entgegenstreckst. Deine Mutterhände bieten mir alle Gnaden für Zeit und Ewigkeit an, die ich brauche, um zu dir und zu deinem göttlichen Sohn ins himmlische Vaterland zu gelangen. Vertrauensvoll erhebe ich meine Hände zu dir, um all diese Gnaden in Empfang zu nehmen. Zugleich danke ich für alle, die du mir schon gegeben hast. Hilf mir, all diese Gnaden treu zu bewahren und mit denselben immer eifrig mitzuwirken. Amen.
    </p>

    <p class="closing-prayer">O Maria, ohne Sünde empfangen, bitte für uns, die wir zu dir unsere Zuflucht nehmen.</p>

    <div class="signature">
      <span class="signature__dot"></span>
      <span class="signature__name">Ordo Caelvarin</span>
    </div>
  </section>
</body>
</html>
```